New Business Cards for 3 companies - print and digital Needed FAST!

We have rebranded our company into three separate companies.
We need new business cards for 8 employees, three of whom need a business card for each company - total of 12 cards.
Pelmary is our property development company.
Velta Brokerage & Management handles property management and real estate transactions.
Oakwren Design Build is our construction company.
Business cards MUST be able to be both printed and function as digital business cards.
No black backgrounds.
Front should be each employee's information and include the logo from their primary company.
Back should include all three logos.
Please see the uploaded spreadsheet for all the information you need for each card. Also uploaded the .png files for each logo as well as the style guide for each logo.

Contact Information for Business Card

See uploaded spreadsheet for information

Font styles to use
Sans Serif
Other font styles liked:
• match style guide if possible

Requirements
Should not have
• No dark backgrounds on the front (on the back OK.) No pictures of employees. Thanks!

```html
<!DOCTYPE html>
<html lang="en">
<head>
<meta charset="utf-8">
<title>Pelmary Business Card</title>
<link href="https://fonts.googleapis.com/css2?family=Mulish:wght@400;600;700;800&family=Montserrat:wght@600;700&family=Oswald:wght@500&display=swap" rel="stylesheet">
<style>
  :root {
    --backdrop: #d3d4d6;
    --green: #80c34b;
    --blue: #1276bb;
    --orange: #f15d27;
    --white: #ffffff;
    --ink: #3a3a3c;
  }
  html, body {
    margin: 0;
    padding: 0;
    width: 1200px;
    height: 900px;
    overflow: hidden;
    background: var(--backdrop);
    font-family: "Mulish", sans-serif;
  }
  .card {
    position: absolute;
    top: 114px;
    width: 387px;
    height: 673px;
    overflow: hidden;
  }
  .card--back { left: 180px; }
  .card--front { left: 636px; background: var(--white); }

  .band {
    position: absolute;
    left: 0;
    width: 100%;
    color: var(--white);
  }
  .band--pelmary { top: 0; height: 219px; background: var(--green); }
  .band--oakwren { top: 219px; height: 235px; background: var(--blue); }
  .band--velta { top: 454px; height: 219px; background: var(--orange); }

  .brand {
    position: absolute;
    display: flex;
    align-items: center;
  }
  .brand__square {
    width: 68px;
    height: 68px;
    flex: none;
  }
  .brand__text { margin-left: 15px; }
  .brand__name {
    font-family: "Montserrat", sans-serif;
    font-weight: 600;
    font-size: 38px;
    line-height: 1;
    letter-spacing: 0.5px;
    padding-bottom: 7px;
    border-bottom: 1px solid currentColor;
  }
  .brand__tagline {
    font-family: "Montserrat", sans-serif;
    font-weight: 600;
    font-size: 12px;
    letter-spacing: 1.6px;
    margin-top: 7px;
  }

  .band--pelmary .brand { left: 56px; top: 68px; }
  .band--pelmary .brand__square { background: var(--white); }
  .band--pelmary .brand__name { border-color: rgba(255,255,255,0.8); }

  .wordmark {
    position: absolute;
    left: 0;
    width: 100%;
    text-align: center;
    font-family: "Montserrat", sans-serif;
    font-weight: 700;
    color: var(--white);
    line-height: 1;
  }
  .band--oakwren .wordmark { top: 76px; font-size: 56px; letter-spacing: 1px; }
  .band--velta .wordmark { top: 64px; font-size: 66px; letter-spacing: 2px; }

  .divider-line {
    position: absolute;
    left: 0;
    width: 100%;
    text-align: center;
    font-family: "Montserrat", sans-serif;
    font-weight: 700;
    color: var(--white);
    line-height: 1;
  }
  .band--oakwren .divider-line { top: 174px; font-size: 17px; letter-spacing: 5px; }
  .band--velta .divider-line { top: 142px; font-size: 15px; letter-spacing: 1.8px; }

  .motto {
    position: absolute;
    right: 57px;
    top: 196px;
    font-family: "Oswald", sans-serif;
    font-weight: 500;
    font-size: 17px;
    line-height: 1.2;
    color: var(--white);
  }

  .card--front .brand { left: 55px; top: 70px; }
  .card--front .brand__square { background: var(--green); }
  .card--front .brand__name { color: var(--ink); border-color: var(--green); }
  .card--front .brand__tagline { color: var(--ink); }

  .details {
    position: absolute;
    left: 0;
    width: 100%;
    text-align: center;
    color: var(--ink);
  }
  .person__name {
    top: 228px;
    font-weight: 700;
    font-size: 24px;
    line-height: 30px;
    letter-spacing: 0.6px;
  }
  .person__role {
    top: 264px;
    font-weight: 600;
    font-size: 16px;
    line-height: 22px;
    color: var(--green);
    letter-spacing: 0.5px;
  }
  .licences {
    top: 301px;
    font-size: 16px;
    line-height: 23px;
    letter-spacing: 0.8px;
  }
  .address {
    top: 398px;
    font-size: 17px;
    line-height: 27px;
    letter-spacing: 0.8px;
  }
  .contact-icons {
    position: absolute;
    top: 474px;
    left: 0;
    width: 100%;
    display: flex;
    justify-content: center;
    gap: 6px;
  }
  .contact-icons svg { width: 17px; height: 17px; }
  .contact {
    top: 497px;
    font-size: 17px;
    line-height: 29px;
    letter-spacing: 1px;
  }
  .contact__phone { letter-spacing: 3px; }
  .contact__label { color: var(--green); font-weight: 700; }
</style>
</head>
<body>

<section class="card card--back" aria-label="Card back with the three company names">
  <div class="band band--pelmary">
    <div class="brand">
      <div class="brand__square"></div>
      <div class="brand__text">
        <div class="brand__name">Pelmary</div>
        <div class="brand__tagline">INVEST. BUILD. MANAGE.</div>
      </div>
    </div>
  </div>
  <div class="band band--oakwren">
    <div class="wordmark">OAKWREN</div>
    <div class="divider-line">DESIGN | BUILD</div>
    <div class="motto">Built Right, Built Oakwren</div>
  </div>
  <div class="band band--velta">
    <div class="wordmark">VELTA</div>
    <div class="divider-line">BROKERAGE | MANAGEMENT</div>
  </div>
</section>

<section class="card card--front" aria-label="Card front with contact details">
  <div class="brand">
    <div class="brand__square"></div>
    <div class="brand__text">
      <div class="brand__name">Pelmary</div>
      <div class="brand__tagline">INVEST. BUILD. MANAGE.</div>
    </div>
  </div>

  <div class="details person__name">Daniel Marsh</div>
  <div class="details person__role">CEO/Owner</div>
  <div class="details licences">IL RE Lic#: 475.018362 Chicago<br>GC Lic #: TGC051938</div>
  <div class="details address">118 N. Linden Ave., Ste 3B,<br>Brookfield IL 60513</div>

  <div class="contact-icons" aria-hidden="true">
    <svg viewBox="0 0 24 24"><path fill="#80c34b" d="M6.6 10.8a15 15 0 0 0 6.6 6.6l2.2-2.2a1 1 0 0 1 1-.25 11.4 11.4 0 0 0 3.6.57 1 1 0 0 1 1 1V20a1 1 0 0 1-1 1A17 17 0 0 1 3 4a1 1 0 0 1 1-1h3.5a1 1 0 0 1 1 1c0 1.25.2 2.45.57 3.57a1 1 0 0 1-.25 1z"/></svg>
    <svg viewBox="0 0 24 24"><rect x="2" y="5" width="20" height="14" fill="#80c34b"/><path d="M2 5l10 8 10-8M2 19l7.5-7M22 19l-7.5-7" fill="none" stroke="#fff" stroke-width="1.5"/></svg>
    <svg viewBox="0 0 24 24" fill="none" stroke="#80c34b" stroke-width="1.8"><circle cx="12" cy="12" r="9"/><ellipse cx="12" cy="12" rx="4" ry="9"/><path d="M3 12h18M5 7h14M5 17h14"/></svg>
  </div>

  <div class="details contact">
    <div class="contact__phone">555-014-2738</div>
    <div><span class="contact__label">Pelmary:</span> 555-019-4462 x101</div>
    <div>dmarsh@pelmary.com</div>
    <div>www.pelmary.com</div>
  </div>
</section>

</body>
</html>
```